Update to Current Website (www.tlcapitalcounsel.example)

5 pages is what I need. This is one cohesive design across all pages.

I would like to create an update to the current website with a fresh look and feel that is mobile compatible.

All content will stay the same. The only thing I want removed from the current content is "Steady returns through every chapter" that is on the main page.

The website address is www.tlcapitalcounsel.example

need the site to be mobile-optimized/responsive

During the contest, you can submit one design or page, and in the handover, once selected, the winner will provide the rest of the pages.

Updates

This has been upgraded to a coded project. Looking for something clean, professional, and goes with my newly designed logo. Please read brief for details! Added Monday, February 1, 2016

Target Market(s)

Consumers

Industry/Entity Type

Financial Planning

Coding

Coded - Design and coding required

Number of Pages Required

5+ page

Requirements
Must have
• Really like squarespace builder Marlowe Template or www.bluefernplanning.example
• Something eye catching, simple, and easy to navigate

```html
<!DOCTYPE html>
<html lang="en">
<head>
<meta charset="utf-8">
<title>T&amp;L Capital Counsel</title>
<link rel="stylesheet" href="https://fonts.googleapis.com/css2?family=Libre+Baskerville:wght@400;700&family=Open+Sans:ital,wght@0,400;0,600;0,700;1,400&display=swap">
<style>
:root{
  --gold:#c68b1c;
  --ink:#1d1d1d;
  --grey:#666;
  --rule:#dcdcdc;
  --panel:#e6e3de;
  --footer:#333333;
  --serif:'Libre Baskerville',Georgia,serif;
  --sans:'Open Sans',Arial,sans-serif;
}
*{margin:0;padding:0;box-sizing:border-box}
html,body{width:769px;height:1200px;overflow:hidden;background:#fff}
body{position:relative;font-family:var(--sans);color:var(--ink)}
.abs{position:absolute}
.hero{left:0;top:0;width:769px;height:272px;background:linear-gradient(180deg,#f3e6d2 0%,#ead3b4 45%,#d9b89a 70%,#b67f88 100%)}
.brand{left:63px;top:18px;font-family:var(--serif);font-size:15px;font-weight:700;color:#3a2e22;display:flex;align-items:center;gap:6px}
.brand i{display:block;width:14px;height:14px;border-radius:50%;background:var(--gold)}
.brand small{display:block;font-size:6px;font-weight:400;color:#5a4a3a;margin-top:2px}
.nav{top:30px;left:275px;display:flex;gap:14px;font-family:var(--serif);font-size:8.5px;color:#222}
.nav a{color:inherit;text-decoration:none}
.nav .active{color:var(--gold)}
.social{left:729px;top:82px;width:40px;height:109px;background:#8a8580;display:flex;flex-direction:column;align-items:center;justify-content:space-around;padding:6px 0}
.social span{width:14px;height:14px;border-radius:50%;background:#fff}
.social b{color:#fff;font-size:18px;font-family:var(--sans)}
.hero-kicker{top:120px;width:769px;text-align:center;font-family:var(--serif);font-size:14px;color:#222}
.hero-title{top:146px;width:769px;text-align:center;font-family:var(--serif);font-size:23px;font-weight:700;color:#111}
.dots{top:240px;left:353px;display:flex;gap:4px}
.dots span{width:14px;height:4px;border-radius:2px;background:#222}
.dots span:first-child{background:var(--gold)}
.welcome{top:307px;width:769px;text-align:center;font-family:var(--serif);font-size:14px}
.divider{top:341px;left:306px;width:157px;height:12px}
.intro{top:370px;width:769px;text-align:center;font-size:7.5px;line-height:16px;color:var(--grey)}
.card{width:198px;height:262px;border:1px solid var(--rule);padding:3px}
.card div{width:100%;height:100%}
.caption{width:198px;text-align:center;font-family:var(--serif);font-size:11px;line-height:17px}
.hr{left:63px;width:642px;height:1px;background:var(--rule)}
.section-title{font-family:var(--serif);font-size:14px}
.thumb{left:63px;width:88px;height:72px;border:1px solid var(--rule);padding:2px}
.thumb div{width:100%;height:100%}
.news-title{left:167px;width:210px;font-size:8.5px;font-weight:700;line-height:16px;text-transform:uppercase;color:#333}
.meta{left:167px;font-size:8px;font-style:italic;color:var(--gold)}
.more{left:282px;width:90px;text-align:right;top:1063px;font-size:8.5px;font-weight:700;color:var(--gold)}
.market{left:419px;top:855px;width:286px}
.market div{height:39px;padding-left:13px;display:flex;align-items:center;font-size:8.5px;font-weight:700;color:#333;background:var(--panel)}
.market div.hi{background:var(--gold);color:#fff}
.delay{left:419px;top:1030px;font-size:8.5px;color:#444}
.footer{left:0;top:1107px;width:769px;height:93px;background:var(--footer)}
.f-brand{left:63px;top:1132px;font-family:var(--serif);font-size:14px;font-weight:700;color:#fff;display:flex;align-items:center;gap:6px}
.f-brand i{display:block;width:12px;height:12px;border-radius:50%;background:#fff}
.copy{top:1136px;width:769px;text-align:center;font-size:7.5px;color:#ddd}
.links{top:1156px;width:769px;text-align:center;font-size:7.5px;color:#ddd;word-spacing:1px}
.badge{left:600px;top:1120px;width:106px;height:60px}
</style>
</head>
<body>
<section class="abs hero" role="img" aria-label="Photo of a surfer mid-leap above ocean spray in warm sunset light"></section>
<div class="abs brand"><i></i><div>T&amp;L Capital Counsel<small>Customized strategies since 1968</small></div></div>
<nav class="abs nav"><a class="active" href="#">HOME</a><a href="#">ABOUT US</a><a href="#">WEALTH MANAGEMENT SERVICES</a><a href="#">RESOURCES</a><a href="#">ACCOUNT ACCESS</a></nav>
<div class="abs social"><span></span><span></span><b>?</b></div>
<p class="abs hero-kicker">CUSTOMIZED STRATEGIES</p>
<h1 class="abs hero-title">FOR YOUR CHANGING SEASON</h1>
<div class="abs dots"><span></span><span></span><span></span><span></span></div>

<h2 class="abs welcome">WELCOME TO T&amp;L CAPITAL COUNSEL</h2>
<svg class="abs divider" viewBox="0 0 157 12"><line x1="0" y1="6" x2="62" y2="6" stroke="#dcdcdc"/><line x1="95" y1="6" x2="157" y2="6" stroke="#dcdcdc"/><circle cx="78.5" cy="6" r="4.5" fill="#c68b1c"/></svg>
<p class="abs intro">At T&amp;L Capital Counsel, our mission is to offer independent and unbiased wealth strategies to individuals, families, and business.<br>We specialize in creating customized income strategies tailored to each client's financial goals.</p>

<div class="abs card" style="left:63px;top:432px"><div role="img" aria-label="Portrait photo of the lead advisor" style="background:linear-gradient(135deg,#cfd8e2,#8a9bb0 60%,#2a3a55)"></div></div>
<div class="abs card" style="left:285px;top:432px"><div role="img" aria-label="Photo of a globe resting on a keyboard with network lines" style="background:linear-gradient(135deg,#e8e8e6,#9a9a98 55%,#3a3a3a)"></div></div>
<div class="abs card" style="left:507px;top:432px"><div role="img" aria-label="Photo of hands over financial charts with glowing graph overlay" style="background:linear-gradient(135deg,#b8b2aa,#e6dccc 45%,#5a5a60)"></div></div>
<p class="abs caption" style="left:63px;top:711px">ABOUT<br>OUR TEAM</p>
<p class="abs caption" style="left:285px;top:711px">MEDIA<br>&amp; NEWSLETTER</p>
<p class="abs caption" style="left:507px;top:711px">COMPLIMENTARY<br>INVESTMENT REVIEWS</p>

<div class="abs hr" style="top:782px"></div>

<h3 class="abs section-title" style="left:63px;top:814px">INDUSTRY NEWS</h3>
<div class="abs thumb" style="top:856px"><div role="img" aria-label="Photo of hands holding a glowing chart" style="background:linear-gradient(135deg,#2b3a4e,#8ea3b8)"></div></div>
<p class="abs news-title" style="top:852px">Channel Nine's Dale Harwick and radio host toy with Reyes VP possibility</p>
<p class="abs meta" style="top:890px">&#9632; 05/02/2016 &nbsp;| &nbsp;&#9679; Sam Porter</p>
<div class="abs hr" style="top:941px;width:307px"></div>
<div class="abs thumb" style="top:958px"><div role="img" aria-label="Photo of a hand writing beside a calculator" style="background:linear-gradient(135deg,#f4f4f4,#b8b8b8)"></div></div>
<p class="abs news-title" style="top:964px">Walt Pemberly to Reyes: it's not 'good for America' to skip Caucus debate</p>
<p class="abs meta" style="top:1002px">&#9632; 05/02/2016 &nbsp;| &nbsp;&#9679; Sam Porter</p>
<div class="abs hr" style="top:1044px;width:307px"></div>
<p class="abs more">VIEW MORE NEWS &gt;&gt;</p>

<h3 class="abs section-title" style="left:419px;top:814px">MARKET SUMMARY</h3>
<div class="abs market"><div class="hi">BLUE CHIP INDEX</div><div>TECH COMPOSITE</div><div class="hi">BROAD MARKET 500</div><div>10 YEAR BOND(%)</div></div>
<p class="abs delay">Quotes delayed atleast 20 minutes..</p>

<footer class="abs footer"></footer>
<div class="abs f-brand"><i></i>T&amp;L Capital Counsel</div>
<p class="abs copy">Copyright © 2016, T&amp;L Capital Counsel. All rights reserved.</p>
<p class="abs links">Home &nbsp;| &nbsp;About us &nbsp;| &nbsp;Wealth Management Services &nbsp;| &nbsp;Resources &nbsp;| &nbsp;Account Access</p>
<svg class="abs badge" viewBox="0 0 106 60" role="img" aria-label="Award badge"><rect x="0" y="0" width="106" height="46" fill="#4a4a4a"/><rect x="0" y="47" width="106" height="13" fill="#c0272d"/></svg>
</body>
</html>
```